Black Hair Stylist Business Card

Looking a for a business card for my hair styling business. Would like the card to be clean and giving our company a sophisticated look. I specialize in black hair styling including braids, sew ins and extensions. I have uploaded two versions of my logo, both are PNG files.

On the front of the card I would like my logo, name (Marisol Trevane), phone number (Will provide number to the winner, for now use a fake number) and the area I service which is Lakemont, WA.

On the back I would like a list of the different styles of hair I do.
Knotless Braids - Feeding Braids - Bohemian Braids - Extensions - Sew In - Crochet - Butterfly Locs - Twist

On the back I would also like to note I have great reviews. Would be nice to have 5 Stars Emojis - GlamNook I may also provide a QR code to take customers to my GlamNook Page.

PLEASE NOTE: Originally I upload 2 versions of our logo. Now that we've seen some options we've decided to go with the pink logo and a white/cream white background.

Target Market(s)

Black Men and Women

Industry/Entity Type

Hair Styling and Design

Contact Information for Business Card

Please refer to the Project Description for details.

Font styles to use
Serif
Sans Serif

Colors
E54698
E96AAD
F1A4CE
F9D9EA
FCEFF6
A7469A
B969AE
D3A5CF
EDDBEB
F8F0F9

Requirements
Must have
• Please refer to the Project Description for details.
Nice to have
• Easy to read and feels sophisticated.
Should not have
• Should not be too busy looking.

```html
<!DOCTYPE html>
<html lang="en">
<head>
<meta charset="utf-8">
<title>Marisol Trevane – Business Card</title>
<link rel="stylesheet" href="https://fonts.googleapis.com/css2?family=Poppins:wght@400;500;600;700&family=Dancing+Script:wght@500&display=swap">
<style>
  :root {
    --backdrop: #e4e4e6;
    --cream: #f8f4ea;
    --ink: #2e2e33;
    --brand-pink: #e5198f;
    --star-gold: #f6b21c;
    --front-violet: #c21bcc;
    --front-pink: #f3157f;
    --white: #ffffff;
  }
  * { margin: 0; padding: 0; box-sizing: border-box; }
  html, body { width: 1200px; height: 1000px; overflow: hidden; }
  body {
    background: radial-gradient(ellipse at 50% 40%, #f1f1f2 0%, var(--backdrop) 70%);
    font-family: "Poppins", sans-serif;
    position: relative;
  }
  .card {
    position: absolute;
    width: 540px;
    height: 300px;
    border-radius: 28px;
    box-shadow: 0 18px 40px rgba(0,0,0,0.12);
    overflow: hidden;
  }
  /* Back of card */
  .card-back {
    left: 90px;
    top: 190px;
    background: var(--cream);
    display: flex;
    align-items: center;
    padding: 0 40px 0 50px;
  }
  .brand-block {
    width: 220px;
    flex: none;
    text-align: center;
  }
  .brand-name {
    font-size: 32px;
    font-weight: 600;
    color: var(--brand-pink);
    line-height: 1.1;
    white-space: nowrap;
  }
  .rating {
    display: flex;
    justify-content: center;
    gap: 6px;
    margin: 14px 0 8px;
  }
  .rating svg { width: 20px; height: 20px; }
  .review-site {
    font-size: 20px;
    font-weight: 700;
    color: var(--ink);
    letter-spacing: 0.5px;
  }
  .style-list {
    list-style: none;
    margin-left: 50px;
    font-size: 16px;
    font-weight: 500;
    color: var(--ink);
    line-height: 1.3;
    white-space: nowrap;
  }
  /* Front of card */
  .card-front {
    left: 570px;
    top: 540px;
    background: linear-gradient(110deg, var(--front-violet) 0%, #e018a8 55%, var(--front-pink) 100%);
    color: var(--white);
    padding: 80px 0 0 70px;
  }
  .stylist-name {
    font-family: "Dancing Script", cursive;
    font-weight: 500;
    font-size: 48px;
    line-height: 1;
    white-space: nowrap;
  }
  .stylist-title {
    font-size: 20px;
    font-weight: 700;
    margin: 8px 0 12px 44px;
  }
  .contact-line {
    display: flex;
    align-items: center;
    gap: 8px;
    font-size: 18px;
    font-weight: 500;
    margin-left: 58px;
    margin-bottom: 4px;
  }
  .contact-line svg { width: 18px; height: 18px; flex: none; }
</style>
</head>
<body>

  <section class="card card-back" aria-label="Business card back">
    <div class="brand-block">
      <div class="brand-name">Halo Braids</div>
      <div class="rating" aria-label="Five star rating">
        <svg viewBox="0 0 24 24"><path fill="var(--star-gold)" d="M12 2l3 6.6 7.2.8-5.4 4.9 1.5 7.1L12 17.8 5.7 21.4l1.5-7.1L1.8 9.4 9 8.6z"/></svg>
        <svg viewBox="0 0 24 24"><path fill="var(--star-gold)" d="M12 2l3 6.6 7.2.8-5.4 4.9 1.5 7.1L12 17.8 5.7 21.4l1.5-7.1L1.8 9.4 9 8.6z"/></svg>
        <svg viewBox="0 0 24 24"><path fill="var(--star-gold)" d="M12 2l3 6.6 7.2.8-5.4 4.9 1.5 7.1L12 17.8 5.7 21.4l1.5-7.1L1.8 9.4 9 8.6z"/></svg>
        <svg viewBox="0 0 24 24"><path fill="var(--star-gold)" d="M12 2l3 6.6 7.2.8-5.4 4.9 1.5 7.1L12 17.8 5.7 21.4l1.5-7.1L1.8 9.4 9 8.6z"/></svg>
        <svg viewBox="0 0 24 24"><path fill="var(--star-gold)" d="M12 2l3 6.6 7.2.8-5.4 4.9 1.5 7.1L12 17.8 5.7 21.4l1.5-7.1L1.8 9.4 9 8.6z"/></svg>
      </div>
      <div class="review-site">GlamNook</div>
    </div>
    <ul class="style-list">
      <li>Knotless Braids</li>
      <li>Feeding Braids</li>
      <li>Bohemian Braids</li>
      <li>Extensions</li>
      <li>Sew In</li>
      <li>Crochet</li>
      <li>Butterfly Locs</li>
      <li>Twist</li>
    </ul>
  </section>

  <section class="card card-front" aria-label="Business card front">
    <div class="stylist-name">Marisol Trevane</div>
    <div class="stylist-title">Black Hair Stylist</div>
    <div class="contact-line">
      <svg viewBox="0 0 24 24"><path fill="var(--white)" d="M6.6 10.8a15.1 15.1 0 0 0 6.6 6.6l2.2-2.2a1 1 0 0 1 1-.25 11.4 11.4 0 0 0 3.6.57 1 1 0 0 1 1 1V20a1 1 0 0 1-1 1A17 17 0 0 1 3 4a1 1 0 0 1 1-1h3.5a1 1 0 0 1 1 1c0 1.250.2 2.45.57 3.6a1 1 0 0 1-.25 1z"/></svg>
      <span>555-018-2346</span>
    </div>
    <div class="contact-line">
      <svg viewBox="0 0 24 24"><path fill="none" stroke="var(--white)" stroke-width="2" d="M12 22s7-6.2 7-12a7 7 0 0 0-14 0c0 5.8 7 12 7 12z"/><circle cx="12" cy="10" r="2.6" fill="none" stroke="var(--white)" stroke-width="2"/></svg>
      <span>Lakemont, WA</span>
    </div>
  </section>

</body>
</html>
```